Medical Billing - Professional Marketing Flier

We are needing help designing a clean and professional looking easy to read marketing flier for a medical billing practice. The text needs to be large enough to print. We are looking for a 5.5 x 8.5 design that we can edit the text as needed. I have included our logo and what we initially want it to say. Please keep in mind, we also want our logo and contact details on the flier. Let me know if you have any questions.

```html
<!DOCTYPE html>
<html lang="en">
<head>
<meta charset="utf-8">
<title>Vega Medical Billing – Flier</title>
<link href="https://fonts.googleapis.com/css2?family=Crimson+Pro:wght@700&family=Montserrat:wght@400;500;600&family=Poppins:wght@300&display=swap" rel="stylesheet">
<style>
  :root {
    --backdrop: #9a989a;
    --paper: #ffffff;
    --ink: #111111;
    --body-ink: #2a2d44;
    --rule: #b35fa5;
    --brand: #7a529e;
    --band-left: #b45ea8;
    --band-right: #6a5ca8;
    --glow-purple: rgba(205, 178, 216, 0.85);
    --glow-blue: rgba(176, 196, 232, 0.7);
    --photo-light: #e9e9ec;
    --photo-dark: #9c9ca3;
    --contact-left: rgba(178, 120, 186, 0.9);
    --contact-right: rgba(130, 122, 192, 0.9);
  }
  * { margin: 0; padding: 0; box-sizing: border-box; }
  html, body { width: 882px; height: 1200px; overflow: hidden; }
  body { background: var(--backdrop); position: relative; font-family: "Montserrat", sans-serif; }

  .flier {
    position: absolute; left: 57px; top: 60px;
    width: 768px; height: 1086px;
    background: var(--paper); overflow: hidden;
  }
  .corner-glow {
    position: absolute; left: 430px; top: 0; width: 338px; height: 300px;
    background:
      radial-gradient(ellipse 60% 55% at 80% 25%, var(--glow-purple), rgba(205,178,216,0) 100%),
      radial-gradient(ellipse 55% 60% at 45% 55%, var(--glow-blue), rgba(176,196,232,0) 100%);
  }

  .brand { position: absolute; left: 44px; top: 62px; display: flex; align-items: center; gap: 10px; color: var(--brand); font-family: "Montserrat", sans-serif; font-weight: 500; }
  .brand-dot { width: 26px; height: 26px; border-radius: 50%; background: var(--brand); }
  .brand-name { line-height: 1; }
  .brand-name .big { display: block; font-size: 38px; letter-spacing: 4px; }
  .brand-name .small { display: block; font-size: 9.5px; letter-spacing: 3px; margin-top: 4px; }

  .headline {
    position: absolute; left: 47px; top: 126px;
    font-family: "Crimson Pro", serif; font-weight: 700;
    font-size: 47.5px; line-height: 44px; color: var(--ink);
    white-space: nowrap; letter-spacing: 0.2px;
  }

  .service { position: absolute; width: 326px; color: var(--body-ink); }
  .service h2 { font-size: 15.8px; font-weight: 500; letter-spacing: 0.4px; line-height: 18px; color: #2b3147; padding-bottom: 5px; border-bottom: 3px solid var(--rule); }
  .service p { margin-top: 12px; font-size: 13px; line-height: 15.5px; white-space: nowrap; }
  .svc-billing { left: 47px; top: 244px; }
  .svc-credential { left: 405px; top: 244px; }
  .svc-aging { left: 48px; top: 446px; }
  .svc-contact { left: 406px; top: 448px; }

  .lower-art { position: absolute; left: 0; top: 600px; width: 768px; height: 486px; }

  .contact-box {
    position: absolute; left: 0; top: 941px; width: 470px; height: 145px;
    border-top-right-radius: 22px;
    background: linear-gradient(90deg, var(--contact-left), var(--contact-right));
    color: #ffffff; font-family: "Poppins", sans-serif; font-weight: 300;
  }
  .contact-line { position: absolute; left: 38px; display: flex; align-items: center; gap: 14px; white-space: nowrap; }
  .contact-line svg { flex: none; }
  .contact-phone { top: 24px; font-size: 40px; letter-spacing: 1px; }
  .contact-email { top: 78px; font-size: 21px; }
  .contact-web { top: 108px; font-size: 21px; }
</style>
</head>
<body>
<main class="flier">
  <div class="corner-glow" role="img" aria-label="Decorative star burst in soft purple and blue"></div>

  <div class="brand">
    <span class="brand-dot"></span>
    <span class="brand-name"><span class="big">VEGA</span><span class="small">MEDICAL BILLING</span></span>
  </div>

  <h1 class="headline">MEDICAL BILLING TAILORED<br>TO YOUR PRACTICES NEEDS</h1>

  <section class="service svc-billing">
    <h2>MEDICAL BILLING</h2>
    <p>Would you prefer to spend time focusing on your<br>clients and running your practice rather than<br>trying to stay up to speed with the constantly<br>changing medical billing rules and regulations?<br>Let us help you by managing your medical billing<br>and dealing with the insurance companies on<br>your behalf! We work with you to tailor the entire<br>medical billing process to suit your practices<br>needs while making it as smooth and painless as<br>possible.</p>
  </section>

  <section class="service svc-credential">
    <h2>CREDENTIALING</h2>
    <p>Are you wanting to get contracted with insurance<br>companies but aren’t sure how to go about it?<br>Are you wanting to expand your client base by<br>having the option to bill insurance? Let us take<br>the confusion out of what can seem like a<br>daunting task! We can get you and your<br>practitioners contracted with the insurance<br>companies of your choice and help you navigate<br>through the process every step of the way!</p>
  </section>

  <section class="service svc-aging">
    <h2>AGING</h2>
    <p>Are you leaving money on the table? Are you able<br>to do the follow-through needed to keep your<br>aging in check and more money flowing into<br>your practice? Are you uncertain about how to<br>get insurance to pay on claims that should be<br>covered but for some reason they decided not to?<br>We can clean up your aging, reduce the amount<br>of time it takes for claims to pay out, and we can<br>keep your aging to a minimum.</p>
  </section>

  <section class="service svc-contact">
    <h2>CONTACT US</h2>
    <p>If any of these processes are something you<br>would like our help with or to consult with us on,<br>please email us or give us a call! We specialize in<br>billing and contracting for Nutritionists and<br>Dietitians. We would love to help you expand<br>your business and take the pain and frustration<br>out of billing so you can focus on your clients.</p>
  </section>

  <svg class="lower-art" viewBox="0 600 768 486">
    <defs>
      <linearGradient id="band" x1="0" y1="0" x2="1" y2="0">
        <stop offset="0" stop-color="var(--band-left)"/>
        <stop offset="1" stop-color="var(--band-right)"/>
      </linearGradient>
      <linearGradient id="photo" x1="0" y1="0" x2="1" y2="1">
        <stop offset="0" stop-color="var(--photo-light)"/>
        <stop offset="0.6" stop-color="#d6d6da"/>
        <stop offset="1" stop-color="var(--photo-dark)"/>
      </linearGradient>
    </defs>
    <path d="M0 757 Q 330 600 768 645 L 768 1086 L 0 1086 Z" fill="url(#band)"/>
    <path d="M0 837 Q 300 700 768 698 L 768 1086 L 0 1086 Z" fill="url(#photo)" role="img" aria-label="Photo of a health insurance form with a stethoscope, pen and calculator"/>
  </svg>

  <div class="contact-box">
    <div class="contact-line contact-phone">
      <svg width="18" height="20" viewBox="0 0 24 24" aria-hidden="true"><path fill="#fff" d="M6.6 10.8a15.1 15.1 0 0 0 6.6 6.6l2.2-2.2c.3-.3.7-.4 1-.2 1.1.4 2.3.6 3.6.6.6 0 1 .4 1 1V20c0 .6-.4 1-1 1A17 17 0 0 1 3 4c0-.6.4-1 1-1h3.5c.6 0 1 .4 1 1 0 1.3.2 2.5.6 3.6.1.3 0 .7-.2 1z"/></svg>
      <span>555-014-0372</span>
    </div>
    <div class="contact-line contact-email">
      <svg width="20" height="15" viewBox="0 0 20 15" aria-hidden="true"><rect x="1" y="1" width="18" height="13" fill="none" stroke="#fff" stroke-width="1.6"/><path d="M1 1 L10 8 L19 1 M1 14 L7.5 7 M19 14 L12.5 7" fill="none" stroke="#fff" stroke-width="1.6"/></svg>
      <span>admin@vegamedicalbilling.com</span>
    </div>
    <div class="contact-line contact-web">
      <svg width="20" height="20" viewBox="0 0 20 20" aria-hidden="true"><g fill="none" stroke="#fff" stroke-width="1.5"><circle cx="10" cy="10" r="8.5"/><ellipse cx="10" cy="10" rx="4" ry="8.5"/><path d="M1.5 10h17M3 5.5h14M3 14.5h14"/></g></svg>
      <span>www.vegamedicalbilling.com</span>
    </div>
  </div>
</main>
</body>
</html>
```